Tidal Crumb Ingredients

Ingredients list/einkorn info. We are looking to improve a 5.5 x 8.5" double sided handout (2 per 8.5 x 11" piece of paper) to hand out with bread and for marketing. Or skinnier 3 per piece of paper? Or suggest a better format. Also to be used in social media and web. And possibly a banner.

Target Market(s)

Healthy, intelligent, yoga, athletic, wealthy

Industry/Entity Type

Bakery

Font styles to use
Sans Serif
Other font styles liked:
• simple readable attractive

Requirements
Must have
• Display the value (and uniqueness) of ingredients
Nice to have
• Well presented info with instant visual appeal. Choose between the 2 logos which you like most. Let us know if you want more photos.
Should not have
• Ornate frills

```html
<!DOCTYPE html>
<html lang="en">
<head>
<meta charset="utf-8">
<title>Tidal Crumb – Ingredients Handout</title>
<link href="https://fonts.googleapis.com/css2?family=Montserrat:wght@400;500;600;700&display=swap" rel="stylesheet">
<style>
  :root {
    --teal: #13aa8c;
    --navy: #114a88;
    --orange: #d68a26;
    --pink: #cf4a8e;
    --white: #ffffff;
    --brown: #5a2d0c;
    --rule: rgba(160, 190, 225, 0.55);
    --backdrop: #e4e4e4;
  }
  * { box-sizing: border-box; margin: 0; padding: 0; }
  html, body { width: 855px; height: 1200px; overflow: hidden; }
  body {
    background: var(--backdrop);
    font-family: "Montserrat", sans-serif;
    position: relative;
  }
  .handout {
    position: absolute;
    left: 209px;
    width: 437px;
    height: 566px;
    background: var(--white);
    overflow: hidden;
    box-shadow: 0 4px 14px rgba(0,0,0,0.18);
  }
  .handout--front { top: 24px; }
  .handout--back { top: 610px; }

  .header-panel {
    position: absolute; left: 0; top: 0;
    width: 437px; height: 140px;
    background: var(--teal);
  }
  .header-corner {
    position: absolute; right: 0; top: 0;
    width: 161px; height: 90px;
    background: var(--white);
  }
  .title-pill {
    position: absolute; left: 16px; top: 16px;
    width: 260px; height: 31px;
    background: var(--orange);
    border-radius: 16px 0 0 16px;
    color: var(--white);
    font-weight: 700; font-size: 13px; letter-spacing: 0.4px;
    line-height: 31px; padding-left: 11px;
    white-space: nowrap;
  }
  .intro {
    position: absolute; left: 16px; top: 61px; width: 250px;
    color: var(--white); font-size: 11.4px; line-height: 13.8px;
    letter-spacing: 0.3px;
  }
  .intro strong { font-weight: 700; }

  .body-panel {
    position: absolute; left: 0; top: 150px;
    width: 437px; height: 326px;
    background: var(--navy);
  }
  .band { position: absolute; left: 0; width: 437px; }
  .band--top { top: 132px; height: 18px; background: var(--pink); }
  .band--pink { top: 476px; height: 18px; background: var(--pink); }
  .band--orange { top: 494px; height: 18px; background: var(--orange); }

  .brand-seal {
    position: absolute; left: 284px; top: 14px;
    width: 146px; height: 146px; border-radius: 50%;
    background: var(--white);
    border: 4px solid var(--teal);
    display: flex; align-items: center; justify-content: center;
    z-index: 2;
  }
  .brand-name {
    color: var(--navy); font-weight: 700; font-size: 18px;
    letter-spacing: 0.5px; text-align: center; line-height: 22px;
  }

  .content {
    position: absolute; left: 16px; top: 167px; width: 407px;
    color: var(--white);
  }
  .section { padding-bottom: 11px; border-bottom: 1px solid var(--rule); margin-bottom: 11px; }
  .section-title {
    font-weight: 600; font-size: 12.6px; letter-spacing: 0.7px;
    display: flex; align-items: center; margin-bottom: 5px; line-height: 15px;
  }
  .section-title::before {
    content: ""; width: 7px; height: 7px; border-radius: 50%;
    background: var(--teal); margin-right: 5px;
  }
  .section-text { font-size: 11.3px; line-height: 13.6px; letter-spacing: 0.3px; }
  .section-text small { font-size: 9.6px; }
  .section--split { display: flex; }
  .section--split .col { flex: 1; }
  .section--split .col + .col { border-left: 1px solid var(--rule); padding-left: 15px; }

  .footnote {
    text-align: center; font-size: 11.3px; line-height: 13.6px; letter-spacing: 0.3px;
    padding-top: 5px;
  }
  .footnote small { font-size: 9.6px; font-weight: 500; }
  .footnote strong { font-weight: 600; }

  .einkorn-pill {
    display: inline-block; background: var(--orange); color: var(--white);
    font-weight: 700; font-size: 12.6px; letter-spacing: 0.5px;
    height: 31px; line-height: 31px; padding: 0 11px; border-radius: 16px;
    margin: 3px 0 15px;
  }
  .benefits { list-style: none; width: 385px; }
  .benefits li {
    position: relative; padding-left: 13px;
    font-size: 11.3px; line-height: 13.9px; letter-spacing: 0.3px;
    margin-bottom: 4.6px;
  }
  .benefits li::before {
    content: ""; position: absolute; left: 0; top: 3.5px;
    width: 7px; height: 7px; border-radius: 50%;
    border: 1.6px solid var(--teal);
  }
  .benefits strong { font-weight: 600; }
  .handout--back .footnote { margin-top: 10px; border-top: 1px solid var(--rule); padding-top: 10px; }

  .contact-bar {
    position: absolute; left: 16px; top: 521px; height: 36px;
    display: flex; align-items: center;
    color: var(--brown); font-weight: 700; font-size: 14px; letter-spacing: 0.4px;
  }
  .contact { display: flex; align-items: center; }
  .contact-icon {
    width: 19px; height: 19px; border-radius: 50%;
    background: var(--teal); margin-right: 9px;
    display: flex; align-items: center; justify-content: center;
  }
  .contact-divider { width: 1px; height: 14px; background: var(--orange); margin: 0 19px 0 20px; }
</style>
</head>
<body>

<article class="handout handout--front">
  <div class="header-panel"></div>
  <div class="header-corner"></div>
  <div class="title-pill">The Transformation Of Bread</div>
  <p class="intro">Nutritious digestible delicious, an<br>alternative to the mutated genetics<br>of modern wheat.</p>

  <div class="body-panel"></div>
  <div class="band band--top"></div>
  <div class="brand-seal"><span class="brand-name">Tidal<br>Crumb</span></div>

  <div class="content">
    <div class="section">
      <div class="section-title">Sprouted grains:</div>
      <p class="section-text">Einkorn, spelt, and a touch of heritage rye <small>(Organically grown<br>on family farms in Winthrop, Washington and Teton Valley, Idaho)</small></p>
    </div>
    <div class="section">
      <div class="section-title">Seeds:</div>
      <p class="section-text">Amaranth, sprouted pumpkin seeds, sprouted quinoa,<br>chia seeds, flaxseed, hemp hearts, sprouted sunflowers seeds</p>
    </div>
    <div class="section section--split">
      <div class="col">
        <div class="section-title">Adaptogens:</div>
        <p class="section-text">Ashwaganda, Maca root</p>
      </div>
      <div class="col">
        <div class="section-title">Mushroom extracts:</div>
        <p class="section-text">Lions mane, cordycept</p>
      </div>
    </div>
    <div class="section">
      <div class="section-title">Extra Ingridient:</div>
      <p class="section-text">Montana glacier well water, Cacao, MCT oil, psyilium husk,<br>Himalayan sea salt, trace minerals, love</p>
    </div>
    <p class="footnote">This bread is well tolerated by people with gluten sensitivities.<br><small>(NOT FOR CELIAC DISEASE)</small></p>
  </div>

  <div class="band band--pink"></div>
  <div class="band band--orange"></div>

  <div class="contact-bar">
    <span class="contact">
      <span class="contact-icon"><svg width="11" height="11" viewBox="0 0 24 24"><path d="M6.6 10.8a15 15 0 0 0 6.6 6.6l2.2-2.2a1 1 0 0 1 1-.25 11.4 11.4 0 0 0 3.6.57 1 1 0 0 1 1 1V20a1 1 0 0 1-1 1A17 17 0 0 1 3 4a1 1 0 0 1 1-1h3.5a1 1 0 0 1 1 1c0 1.25.2 2.45.57 3.57a1 1 0 0 1-.25 1z" fill="#fff"/></svg></span>406-555-0142
    </span>
    <span class="contact-divider"></span>
    <span class="contact">
      <span class="contact-icon"><svg width="11" height="11" viewBox="0 0 24 24"><rect x="3" y="5" width="18" height="14" rx="2" fill="none" stroke="#fff" stroke-width="2"/><path d="M3 7l9 6 9-6" fill="none" stroke="#fff" stroke-width="2"/></svg></span>hello@tidalcrumb.com
    </span>
  </div>
</article>

<article class="handout handout--back">
  <div class="header-panel"></div>
  <div class="header-corner"></div>
  <div class="title-pill">Einkorn Grain Vs 'Modern Wheat'</div>
  <p class="intro"><strong>Einkorn</strong> is the original, non-altered<br>wheat grain. It's genetic purity is over<br><strong>10,000</strong> years old.</p>

  <div class="body-panel"></div>
  <div class="band band--top"></div>
  <div class="brand-seal"><span class="brand-name">Tidal<br>Crumb</span></div>

  <div class="content">
    <div class="einkorn-pill">Einkorn is</div>
    <ul class="benefits">
      <li>25% higher in protein and lower in carbohydrates than<br>modern wheat.</li>
      <li>3-4 times more beta-carotene.</li>
      <li>2 times more vitamin A.</li>
      <li>4 times more antioxidants lutein and riboflavin.</li>
      <li>5-6 times more expensive $$$.</li>
      <li>Richer in carotenoids, B vitamins, and essential and<br>trace minerals.</li>
      <li>Non-processed, non-hybridized, non-GMO, non- mutated<br>and has a low glycemic load, meaning <strong>it won’t spike your<br>blood sugar level.</strong></li>
      <li><strong>And It tastes better.</strong></li>
    </ul>
    <p class="footnote">Einkorn <strong>lacks the gluten proteins that trigger symptoms<br>of gluten sensitivity.</strong></p>
  </div>

  <div class="band band--pink"></div>
  <div class="band band--orange"></div>

  <div class="contact-bar">
    <span class="contact">
      <span class="contact-icon"><svg width="11" height="11" viewBox="0 0 24 24"><path d="M6.6 10.8a15 15 0 0 0 6.6 6.6l2.2-2.2a1 1 0 0 1 1-.25 11.4 11.4 0 0 0 3.6.57 1 1 0 0 1 1 1V20a1 1 0 0 1-1 1A17 17 0 0 1 3 4a1 1 0 0 1 1-1h3.5a1 1 0 0 1 1 1c0 1.25.2 2.45.57 3.57a1 1 0 0 1-.25 1z" fill="#fff"/></svg></span>406-555-0142
    </span>
    <span class="contact-divider"></span>
    <span class="contact">
      <span class="contact-icon"><svg width="11" height="11" viewBox="0 0 24 24"><rect x="3" y="5" width="18" height="14" rx="2" fill="none" stroke="#fff" stroke-width="2"/><path d="M3 7l9 6 9-6" fill="none" stroke="#fff" stroke-width="2"/></svg></span>hello@tidalcrumb.com
    </span>
  </div>
</article>

</body>
</html>
```